Simple Slide from Excel on History of Technology

I need to convert this timeline into a more readable and friendly slide for a report I am doing. It is in Excel format. Feel free to cut some of the words and make it more simple. It can be in Word, powerpoint or excel.

Target Market(s)

a school paper, a professor will see

Requirements
Must have
• should give a feeling of momentum over time. Please add the number of internet users for each year it is available as 1,000 in 1975, 30,000 in 1987, 14 million in 1993, 25 million in 1994, 45 million in 1995, 77 million in 1996, 121 million in 1997, 188 million in 1998, 281 million in 1999, 413 million in 2000, 910 million in 2004, 1.4 billion in 2007

```html
<!DOCTYPE html>
<html lang="en">
<head>
<meta charset="utf-8">
<title>The History of the Internet</title>
<link rel="stylesheet" href="https://fonts.googleapis.com/css2?family=Bebas+Neue&family=Open+Sans:wght@400;600;700&display=swap">
<style>
  :root {
    --page-bg: #d6d6d6;
    --sheet: #ffffff;
    --header-deep: #2a46c9;
    --header-light: #5d93ea;
    --orange-soft: #f7a15a;
    --orange: #f26b22;
    --red: #d7191f;
    --blue: #1e7bd3;
    --green: #7ab73a;
    --ink: #2b2b2b;
    --line: #5a5a5a;
    --band-light: #92bbf5;
    --band-deep: #3853c6;
  }
  html, body { margin: 0; padding: 0; }
  body {
    width: 1200px; height: 1200px; overflow: hidden;
    background: var(--page-bg);
    position: relative;
    font-family: "Open Sans", Arial, sans-serif;
  }
  .poster {
    position: absolute; left: 176px; top: 0;
    width: 988px; height: 1398px;
    background: var(--sheet);
    transform: scale(0.8584); transform-origin: top left;
    box-shadow: 0 4px 18px rgba(0,0,0,0.25);
    overflow: hidden;
  }
  .poster-header {
    position: absolute; left: 0; top: 0; width: 988px; height: 243px;
    background: radial-gradient(circle at 50% 60%, var(--header-light) 0%, var(--header-deep) 70%);
  }
  .poster-title {
    position: absolute; left: 0; top: 68px; width: 988px; margin: 0;
    text-align: center; color: #fff;
    font-family: "Bebas Neue", "Arial Narrow", sans-serif;
    font-weight: 400; font-size: 76px; letter-spacing: 0.5px;
  }
  .timeline { position: absolute; left: 0; top: 243px; width: 988px; height: 1039px; }
  .timeline svg { display: block; }
  .yr { font-family: "Open Sans", Arial, sans-serif; font-size: 12.5px; font-weight: 700; }
  .desc { font-family: "Open Sans", Arial, sans-serif; font-size: 10.5px; fill: var(--ink); }
  .brand { font-family: "Open Sans", Arial, sans-serif; font-size: 8px; font-weight: 700; fill: var(--ink); text-anchor: middle; }
  .glyph { font-family: "Open Sans", Arial, sans-serif; font-weight: 700; fill: #111; text-anchor: middle; }
  .end { text-anchor: end; }
  .c-os { fill: var(--orange-soft); } .c-o { fill: var(--orange); } .c-r { fill: var(--red); }
  .c-b { fill: var(--blue); } .c-g { fill: var(--green); }
  .dot { fill: #fff; stroke-width: 2.5; }
  .ring { fill: #fff; stroke-width: 2.8; }
  .link { stroke: var(--line); stroke-width: 1.2; }
  .s-os { stroke: var(--orange-soft); } .s-o { stroke: var(--orange); } .s-r { stroke: var(--red); }
  .s-b { stroke: var(--blue); } .s-g { stroke: var(--green); }
  .ico { fill: none; stroke: #111; stroke-width: 1.6; }
  .ico-fill { fill: #111; }
  .credit-band {
    position: absolute; left: 0; top: 1282px; width: 988px; height: 40px;
    background: var(--band-light);
    display: flex; align-items: center; justify-content: center;
    font-size: 12.5px; color: #1d2a55;
  }
  .footer-band { position: absolute; left: 0; top: 1322px; width: 988px; height: 76px; background: var(--band-deep); }
</style>
</head>
<body>
<div class="poster">
  <div class="poster-header" role="img" aria-label="Blue circuit-board network pattern behind the title"></div>
  <h1 class="poster-title">The History of the Internet</h1>

  <div class="timeline">
    <svg width="988" height="1039" viewBox="0 243 988 1039" xmlns="http://www.w3.org/2000/svg">
      <!-- connector lines -->
      <g class="link">
        <line x1="408" y1="327" x2="485" y2="327"/><line x1="485" y1="360" x2="563" y2="360"/>
        <line x1="408" y1="394" x2="485" y2="394"/><line x1="408" y1="462" x2="485" y2="462"/>
        <line x1="485" y1="496" x2="563" y2="496"/><line x1="408" y1="530" x2="485" y2="530"/>
        <line x1="485" y1="563" x2="563" y2="563"/><line x1="408" y1="597" x2="485" y2="597"/>
        <line x1="408" y1="665" x2="485" y2="665"/><line x1="485" y1="699" x2="563" y2="699"/>
        <line x1="408" y1="733" x2="485" y2="733"/><line x1="485" y1="767" x2="563" y2="767"/>
        <line x1="408" y1="801" x2="485" y2="801"/><line x1="485" y1="834" x2="563" y2="834"/>
        <line x1="408" y1="868" x2="485" y2="868"/><line x1="485" y1="902" x2="563" y2="902"/>
        <line x1="408" y1="1003" x2="485" y2="1003"/><line x1="485" y1="1104" x2="563" y2="1104"/>
        <line x1="408" y1="1138" x2="485" y2="1138"/><line x1="485" y1="1171" x2="563" y2="1171"/>
        <line x1="408" y1="1205" x2="485" y2="1205"/><line x1="485" y1="1239" x2="563" y2="1239"/>
      </g>

      <!-- timeline dots -->
      <circle class="dot s-os" cx="485" cy="292" r="6"/>
      <g class="s-o">
        <circle class="dot" cx="485" cy="327" r="6"/><circle class="dot" cx="485" cy="360" r="6"/>
        <circle class="dot" cx="485" cy="394" r="6"/><circle class="dot" cx="485" cy="428" r="6"/>
        <circle class="dot" cx="485" cy="462" r="6"/><circle class="dot" cx="485" cy="496" r="6"/>
        <circle class="dot" cx="485" cy="530" r="6"/><circle class="dot" cx="485" cy="563" r="6"/>
      </g>
      <g class="s-r">
        <circle class="dot" cx="485" cy="597" r="6"/><circle class="dot" cx="485" cy="631" r="6"/>
        <circle class="dot" cx="485" cy="665" r="6"/><circle class="dot" cx="485" cy="699" r="6"/>
        <circle class="dot" cx="485" cy="733" r="6"/><circle class="dot" cx="485" cy="767" r="6"/>
      </g>
      <g class="s-b">
        <circle class="dot" cx="485" cy="801" r="6"/><circle class="dot" cx="485" cy="834" r="6"/>
        <circle class="dot" cx="485" cy="868" r="6"/><circle class="dot" cx="485" cy="902" r="6"/>
        <circle class="dot" cx="485" cy="936" r="6"/><circle class="dot" cx="485" cy="969" r="6"/>
        <circle class="dot" cx="485" cy="1003" r="6"/><circle class="dot" cx="485" cy="1037" r="6"/>
      </g>
      <g class="s-g">
        <circle class="dot" cx="485" cy="1071" r="6"/><circle class="dot" cx="485" cy="1104" r="6"/>
        <circle class="dot" cx="485" cy="1138" r="6"/><circle class="dot" cx="485" cy="1171" r="6"/>
        <circle class="dot" cx="485" cy="1205" r="6"/><circle class="dot" cx="485" cy="1239" r="6"/>
      </g>

      <!-- icon rings -->
      <g class="s-o">
        <circle class="ring" cx="408" cy="327" r="17"/><circle class="ring" cx="563" cy="360" r="17"/>
        <circle class="ring" cx="408" cy="394" r="17"/><circle class="ring" cx="408" cy="462" r="17"/>
        <circle class="ring" cx="563" cy="496" r="17"/><circle class="ring" cx="408" cy="530" r="17"/>
        <circle class="ring" cx="563" cy="563" r="17"/>
      </g>
      <g class="s-r">
        <circle class="ring" cx="408" cy="597" r="17"/><circle class="ring" cx="408" cy="665" r="17"/>
        <circle class="ring" cx="563" cy="699" r="17"/><circle class="ring" cx="408" cy="733" r="17"/>
        <circle class="ring" cx="563" cy="767" r="17"/>
      </g>
      <g class="s-b">
        <circle class="ring" cx="408" cy="801" r="17"/><circle class="ring" cx="563" cy="834" r="17"/>
        <circle class="ring" cx="408" cy="868" r="17"/><circle class="ring" cx="563" cy="902" r="17"/>
        <circle class="ring" cx="408" cy="1003" r="17"/>
      </g>
      <g class="s-g">
        <circle class="ring" cx="563" cy="1104" r="17"/><circle class="ring" cx="408" cy="1138" r="17"/>
        <circle class="ring" cx="563" cy="1171" r="17"/><circle class="ring" cx="408" cy="1205" r="17"/>
        <circle class="ring" cx="563" cy="1239" r="17"/>
      </g>

      <!-- icons -->
      <g class="ico">
        <path d="M400 335 v-10 h16 v10 z M398 325 l10 -7 l10 7"/>
        <path d="M399 389 h18 v11 h-18 z M399 393 h18 M399 397 h18"/>
        <path d="M400 466 q0 -10 10 -10 l-3 -3 M410 456 l-3 3 M416 458 q0 10 -10 10 l3 3 M406 468 l3 -3"/>
        <path d="M553 493 h20 v8 h-20 z M557 493 l-3 -5 M569 493 l3 -5"/>
        <path d="M399 524 h18 v12 h-18 z M399 524 l9 7 l9 -7"/>
        <path d="M553 559 q0 -4 5 -4 h10 q5 0 5 4 v5 q0 4 -4 3 l-3 -3 h-6 l-3 3 q-4 1 -4 -3 z"/>
        <path d="M555 703 q-4 0 -4 -4 q0 -4 4 -4 q1 -5 6 -5 q5 0 6 4 q5 0 5 5 q0 4 -4 4 z"/>
        <circle cx="408" cy="733" r="9"/><path d="M399 733 h18 M408 724 q-6 9 0 18 q6 -9 0 -18"/>
        <circle cx="408" cy="799" r="8"/><circle cx="408" cy="799" r="3"/><path d="M402 810 h12"/>
        <circle cx="563" cy="834" r="8"/><path d="M563 834 v-8 M563 834 l7 4"/>
        <path d="M556 901 h14 v9 h-14 z M559 901 v-4 q4 -5 8 0 v4"/>
      </g>
      <text class="glyph" x="563" y="367" font-size="20">@</text>
      <text class="glyph" x="408" y="602" font-size="14">:-)</text>
      <text class="glyph" x="408" y="669" font-size="9.5">www</text>

      <!-- invented names in place of marks -->
      <text class="brand" x="563" y="770">Orbit</text>
      <text class="brand" x="408" y="871">Navi</text>
      <text class="brand" x="408" y="1006">Seekly</text>
      <text class="brand" x="563" y="1107">Opedia</text>
      <text class="brand" x="408" y="1141">Pals</text>
      <text class="brand" x="563" y="1174">Vidzy</text>
      <text class="brand" x="408" y="1208">Chirp</text>
      <text class="brand" x="563" y="1242">Pome</text>

      <!-- entries: left side -->
      <text class="yr c-os end" x="468" y="290">1969</text>
      <text class="desc end" x="468" y="303">First Network - Archnet</text>
      <text class="yr c-o end" x="468" y="357">1971</text>
      <text class="desc end" x="468" y="370">Email developed by Ross Talbot. First used @ symbol</text>
      <text class="yr c-o end" x="468" y="416">1974</text>
      <text class="desc end" x="468" y="429">The Beginning of TCP/IP (transmission control protocol),</text>
      <text class="desc end" x="468" y="440">links Archnet networks with no central control</text>
      <text class="yr c-o end" x="468" y="492">1976</text>
      <text class="desc end" x="468" y="504">PC Modem created for computer hobbyists</text>
      <text class="yr c-o end" x="468" y="561">1979</text>
      <text class="desc end" x="468" y="573">Earliest form of multiplayer games, all text</text>
      <text class="yr c-r end" x="468" y="628">1983</text>
      <text class="desc end" x="468" y="640">Archnet switch to TCP/IP</text>
      <text class="yr c-r end" x="468" y="696">1987</text>
      <text class="desc end" x="468" y="708">30,000 hosts on the Internet having grown from 1,000 limit by Archnet</text>
      <text class="yr c-r end" x="468" y="754">1989</text>
      <text class="desc end" x="468" y="767">Orbit is launched, increased popularity of the internet across average users</text>
      <text class="desc end" x="468" y="778">Alan Verity proposed the world wide web at NORDLAB</text>
      <text class="yr c-b end" x="468" y="822">1993</text>
      <text class="desc end" x="468" y="835">First graphical web browser to make the internet easy to use for non-techies</text>
      <text class="desc end" x="468" y="846">(14 million internet users)</text>
      <text class="yr c-b end" x="468" y="889">1995</text>
      <text class="desc end" x="468" y="902">Commericalization of the internet, SSL (secure sockets layer)</text>
      <text class="desc end" x="468" y="913">encryption made it safer to conduct financial transactions  (45 million internet users)</text>
      <text class="yr c-b end" x="468" y="966">1997</text>
      <text class="desc end" x="468" y="978">121 million internet users</text>
      <text class="yr c-b end" x="468" y="1037">1999</text>
      <text class="desc end" x="468" y="1049">281 million internet users</text>
      <text class="yr c-g end" x="468" y="1102">2001</text>
      <text class="desc end" x="468" y="1114">Opedia launched</text>
      <text class="yr c-g end" x="468" y="1168">2005</text>
      <text class="desc end" x="468" y="1180">Vidzy starts</text>
      <text class="yr c-g end" x="468" y="1235">2007</text>
      <text class="desc end" x="468" y="1247">pomePhone (1.4 billion internet users)</text>

      <!-- entries: right side -->
      <text class="yr c-o" x="505" y="324">1970</text>
      <text class="desc" x="505" y="336">Archnet expanded to Universities</text>
      <text class="yr c-o" x="505" y="391">1973</text>
      <text class="desc" x="505" y="403">First connection outside the U.S. - Kingsgate College</text>
      <text class="yr c-o" x="505" y="459">1975</text>
      <text class="desc" x="505" y="471">First Email program - added Reply and Forward capability (1000)</text>
      <text class="yr c-o" x="505" y="526">1978</text>
      <text class="desc" x="505" y="538">First Spam email sent by Gil Tanner to Archnet Users</text>
      <text class="yr c-r" x="505" y="592">1982</text>
      <text class="desc" x="505" y="604">First emoticon :-), a smily face by Sean Farrow</text>
      <text class="yr c-r" x="505" y="660">1984</text>
      <text class="desc" x="505" y="672">Domain Name System created, www.example.com, links user friendly names to IP addresses</text>
      <text class="yr c-r" x="503" y="719">1988</text>
      <text class="desc" x="503" y="732">Internet Rely Chat created, set up capabilty for real-time chat, instant messaging</text>
      <text class="desc" x="503" y="744">also, First malicious internet based attack "the harlan worm" occurred.</text>
      <text class="yr c-b" x="505" y="787">1991</text>
      <text class="desc" x="505" y="799">Alan Verity proposed the world wide web at NORDLAB, First search protocal,</text>
      <text class="desc" x="505" y="811">set up search engines, First webcam</text>
      <text class="yr c-b" x="505" y="853">1994</text>
      <text class="desc" x="505" y="865">first .org and .gov sites for nonprofits and the government's general use</text>
      <text class="desc" x="505" y="877">Navi Explorer launched, a much easier web browser.  Became a standard (25 million users)</text>
      <text class="yr c-b" x="505" y="933">1996</text>
      <text class="desc" x="505" y="945">77 million internet users</text>
      <text class="yr c-b" x="501" y="999">1998</text>
      <text class="desc" x="501" y="1012">Seekly went live!  (188 mil)</text>
      <text class="yr c-g" x="505" y="1068">2000</text>
      <text class="desc" x="505" y="1081">413 million internet users</text>
      <text class="yr c-g" x="506" y="1133">2004</text>
      <text class="desc" x="506" y="1146">Pals opens, social media starts (910 million internet users)</text>
      <text class="yr c-g" x="506" y="1199">2006</text>
      <text class="desc" x="506" y="1212">Chirp starts</text>
    </svg>
  </div>

  <div class="credit-band">credit www.netfolio-studio.com/blog/web-design/the-internet-story-in-brief/</div>
  <div class="footer-band"></div>
</div>
</body>
</html>
```